Redesign of our homepage

We are a company that operates in the Wellness tourism sector. We are starting a project to redesign our homepage. See the screenshots. The main idea is that the banner image and the text on the banner are dynamically replaced depending on whether a user clicks on the "Thumb up" or the "Thumb down" icon.
You can see a live version of our homepage at http://demo.velqorambe.com

Requirements
Must have
• Must abide by style and look & feel of the current site.
It is important to demonstrate the functionality that enables the banner image and text being refreshed at each click of a ThumbUp or ThumbDown icons. In others words the Javascript must work.

Let me add some more context on the project.

Actually the thumb up and thumb down are possible answers to question/comment dynamically displayed at the location of the current text "Experience That Make You tell an unforgettable story".
An example of a comment/question is "I need a program that would help limit my stress levels and make me look great and feel fantastic". Or "I need an activity that will reduce my stress."
So a user would have to click on a thumb up or thumb down to approve or disapprove these questions/comments..
Based on this information, I think you could move the thumbs up to the left and right side of the text (the comment/question) respectively. And move the reset underneath in the middle.

Maybe it's a good idea to reduce the font size of that text as well.

And now to the dropdown list. We need only 2 of them, and not 3 as you have displayed.
One of them contain the list:
-- I need a weekend retreat
-- ! need a week or more retreat
The other would contain a list of countries.
The drop down values must be selected before the thumbs up and down thumbs are active.
Therefore you should move them above the question/comment text.
And finally about the thumbs and reset icons. Please put them in a round orange color and make them a bit bigger.

```html
<!DOCTYPE html>
<html lang="en">
<head>
<meta charset="utf-8">
<title>Velqorambe – Wellness Retreats</title>
<link href="https://fonts.googleapis.com/css2?family=Bebas+Neue&family=Poppins:wght@400;500;600;700&display=swap" rel="stylesheet">
<style>
:root{
  --orange:#f39322;
  --orange-dark:#e57f10;
  --ink:#1f1f1f;
  --text:#555a5f;
  --muted:#8a8f94;
  --line:#e6e6e6;
  --footer:#212121;
  --white:#ffffff;
  --green:#6cc24a;
  --red:#e03a3a;
  --teal:#86dcc0;
  --teal-dark:#5fbfa2;
  --blue:#1f5fa8;
}
*{box-sizing:border-box;margin:0;padding:0}
html,body{width:1200px;height:4251px;overflow:hidden}
body{position:relative;background:var(--white);font-family:"Poppins",sans-serif;color:var(--text);font-size:14px}
.abs{position:absolute}
.display{font-family:"Bebas Neue",sans-serif;font-weight:400;letter-spacing:.3px}

/* header */
.site-header{position:absolute;left:0;top:0;width:1200px;height:101px;background:var(--white)}
.brand{position:absolute;left:87px;top:28px;display:flex;align-items:center;gap:8px;font-size:34px;font-weight:400;color:var(--orange);letter-spacing:.5px}
.brand-dot{width:14px;height:14px;border-radius:50%;background:var(--orange)}
.main-nav{position:absolute;left:380px;top:40px;display:flex;gap:36px;font-size:12.5px;font-weight:500;color:#333;letter-spacing:.3px}
.btn-auth{position:absolute;top:28px;height:40px;border-radius:3px;color:var(--white);font-size:13px;font-weight:600;display:flex;align-items:center;justify-content:center;gap:6px}
.btn-signin{left:888px;width:109px;background:#4a4d50}
.btn-signup{left:1002px;width:109px;background:var(--orange)}

/* hero */
.hero{position:absolute;left:0;top:101px;width:1200px;height:612px;background:linear-gradient(160deg,#55626a 0%,#2f3a40 45%,#1b2226 100%)}
.hero-select{position:absolute;top:112px;height:51px;width:300px;background:var(--white);border-radius:2px;display:flex;align-items:center;gap:10px;padding:0 16px;font-size:13px;color:#555}
.hero-select .caret{margin-left:auto;color:#777;font-size:12px}
.hero-question{position:absolute;left:330px;width:540px;top:222px;text-align:center;color:var(--white);font-size:44px;line-height:46px}
.hero-sub{position:absolute;left:330px;width:540px;text-align:center;color:var(--white);font-size:22px;top:326px}
.thumb-btn{position:absolute;width:88px;height:88px;border-radius:50%;background:var(--orange);display:flex;align-items:center;justify-content:center;box-shadow:0 4px 14px rgba(0,0,0,.25)}
.thumb-up{left:218px;top:224px}
.thumb-down{left:894px;top:224px}
.thumb-reset{left:556px;top:398px;border:4px solid #ffffff55}

/* sidebar */
.filter-head{position:absolute;left:89px;top:800px;width:259px;height:50px;background:var(--orange);color:var(--white);font-weight:700;font-size:15.5px;letter-spacing:.5px;display:flex;align-items:center;justify-content:space-between;padding:0 18px}
.filter-panel{position:absolute;left:89px;top:850px;width:259px;height:579px;background:var(--white);box-shadow:0 4px 16px rgba(0,0,0,.09)}
.filter-row{position:absolute;left:18px;width:223px;display:flex;justify-content:space-between;align-items:center;font-weight:700;font-size:15.5px;color:#3a3a3a;letter-spacing:.3px}
.filter-sep{position:absolute;left:18px;width:223px;height:1px;background:var(--line)}
.cat-head{position:absolute;left:17px;top:142px;width:219px;height:41px;background:#4d5054;color:var(--white);font-weight:700;font-size:15.5px;display:flex;align-items:center;padding:0 0 0 13px}
.cat-row{position:absolute;left:36px;width:200px;display:flex;justify-content:space-between;align-items:center;font-size:16px;color:#555}
.chev{color:#999;font-size:14px}

/* results bar */
.results-count{position:absolute;left:389px;top:807px;font-size:14px;color:#555}
.view-grid{position:absolute;left:696px;top:799px;width:37px;height:37px;border-radius:50%;background:#5c6064;display:flex;align-items:center;justify-content:center}
.view-list{position:absolute;left:745px;top:808px}
.sort-label{position:absolute;left:879px;top:807px;font-size:14px;color:#555}
.sort-select{position:absolute;left:945px;top:797px;width:165px;height:43px;border:1px solid #ddd;border-radius:2px;font-size:14px;color:#555;display:flex;align-items:center;justify-content:space-between;padding:0 12px}

/* cards */
.trip-card{position:absolute;left:391px;width:718px;height:727px;background:var(--white);box-shadow:0 6px 20px rgba(0,0,0,.08)}
.trip-photo{position:absolute;left:0;top:0;width:718px;height:323px}
.fav{position:absolute;left:32px;top:29px;width:57px;height:57px;border-radius:50%;background:var(--white);display:flex;align-items:center;justify-content:center}
.trip-title{position:absolute;left:40px;top:348px;width:660px;font-size:33px;line-height:31px;color:var(--ink);white-space:nowrap}
.trip-price{position:absolute;left:40px;top:421px;font-size:17px;color:#555}
.trip-price b{font-size:27px;color:var(--orange);font-weight:700;margin-left:6px}
.card-rule{position:absolute;left:40px;top:472px;width:632px;height:1px;background:var(--line)}
.col-rule{position:absolute;left:332px;top:473px;width:1px;height:140px;background:var(--line)}
.price-for{position:absolute;left:40px;top:484px;font-size:16px;font-weight:600;color:#333}
.facts{position:absolute;left:40px;top:517px;list-style:none}
.facts li,.perks li{height:27px;display:flex;align-items:center;gap:8px;font-size:15px;color:#666}
.perks{position:absolute;left:366px;top:517px;width:290px;list-style:none}
.perks li span.lbl{flex:1}
.btn-details{position:absolute;left:40px;top:647px;width:269px;height:48px;background:var(--orange);color:var(--white);font-weight:700;font-size:18px;letter-spacing:.5px;display:flex;align-items:center;justify-content:center;gap:34px}
.impact{position:absolute;top:659px;display:flex;align-items:center;gap:7px;font-size:15px;font-weight:600;color:#222}

/* pagination */
.pager{position:absolute;top:3182px;height:28px;font-size:13px;color:#444;display:flex;align-items:center;justify-content:center}
.pg-prev{left:754px;width:79px;background:#ebebeb;color:#555}
.pg-next{left:1030px;width:80px;background:#1b1b1b;color:var(--white);font-weight:600}
.pg-num{position:absolute;top:3186px;font-size:14px;color:#444}
.pg-active{position:absolute;left:884px;top:3182px;width:29px;height:29px;border-radius:50%;background:var(--orange);color:var(--white);font-size:13px;display:flex;align-items:center;justify-content:center}

/* footer */
.site-footer{position:absolute;left:0;top:3732px;width:1200px;height:519px;background:var(--footer)}
.impact-card{position:absolute;top:3328px;width:494px;height:459px;background:var(--white);border-bottom:4px solid var(--orange);box-shadow:0 4px 18px rgba(0,0,0,.06)}
.impact-title{position:absolute;left:0;top:44px;width:100%;text-align:center;font-size:33px;color:var(--ink)}
.impact-sub{position:absolute;left:0;top:82px;width:100%;text-align:center;font-size:14px;color:#777}
.legend{position:absolute;left:52px;top:368px;width:361px;height:34px;border:1px solid #999;font-size:8px;color:#666;padding:4px 6px;line-height:12px}
.legend i{display:inline-block;width:7px;height:7px;border-radius:50%;margin-right:4px;vertical-align:middle}
.foot-col{position:absolute;top:3880px;color:#e6e6e6;font-size:13.5px;line-height:23px}
.foot-col h4{font-family:"Bebas Neue",sans-serif;font-weight:400;font-size:22px;color:var(--white);margin-bottom:14px;letter-spacing:.5px;line-height:24px}
.contact-row{display:flex;align-items:center;gap:10px;margin-bottom:30px}
.socials{display:flex;gap:10px;margin-top:-6px}
.socials span{width:32px;height:32px;border-radius:50%;background:#3a3a3a;display:block}
.foot-rule{position:absolute;left:87px;top:4191px;width:1023px;height:1px;background:#3d3d3d}
.copyright{position:absolute;left:0;top:4207px;width:1200px;text-align:center;font-family:"Bebas Neue",sans-serif;font-size:18px;color:#eee;letter-spacing:.4px}
.to-top{position:absolute;left:1132px;top:4166px;width:40px;height:40px;border-radius:50%;background:var(--orange);display:flex;align-items:center;justify-content:center}
</style>
</head>
<body>

<header class="site-header">
  <div class="brand">velqorambe<span class="brand-dot"></span></div>
  <nav class="main-nav">
    <span>EUR ▾</span><span>WELLNESS RETREATS</span><span>OUR CLIMATE PLEDGE</span><span>PARTNERS</span>
  </nav>
  <div class="btn-auth btn-signin">
    <svg width="14" height="14" viewBox="0 0 14 14"><path d="M5 1h7v12H5M1 7h7M6 4l3 3-3 3" fill="none" stroke="#fff" stroke-width="1.6"/></svg>SIGN IN</div>
  <div class="btn-auth btn-signup">
    <svg width="13" height="14" viewBox="0 0 13 14"><circle cx="6.5" cy="4" r="3.2" fill="#fff"/><path d="M0.5 14c0-4 2.7-6 6-6s6 2 6 6z" fill="#fff"/></svg>SIGN UP</div>
</header>

<section class="hero" role="img" aria-label="Hiker with backpack standing on a rocky sea cliff above crashing waves">
  <div class="hero-select" style="left:288px">
    <svg width="15" height="14" viewBox="0 0 15 14"><rect x="1" y="2" width="13" height="11" fill="none" stroke="#888" stroke-width="1.2"/><path d="M1 5h13M4 0v3M11 0v3" stroke="#888" stroke-width="1.2"/></svg>I need a weekend retreat<span class="caret">⌄</span></div>
  <div class="hero-select" style="left:612px">
    <svg width="9" height="12" viewBox="0 0 9 12"><path d="M4.5 0C2 0 0 2 0 4.4 0 7.6 4.5 12 4.5 12S9 7.6 9 4.4C9 2 7 0 4.5 0z" fill="#777"/><circle cx="4.5" cy="4.4" r="1.6" fill="#fff"/></svg>Where do you want to go?<span class="caret">⌄</span></div>

  <div class="thumb-btn thumb-up">
    <svg width="38" height="36" viewBox="0 0 32 30"><rect x="1" y="12" width="7" height="17" fill="#fff"/><path d="M10 13l6-11c2 0 3 1.5 2.5 4L17 11h10c2 0 3 1.5 2.6 3.2l-2.5 11.5c-.3 1.6-1.6 2.8-3.2 2.8H10z" fill="#fff"/></svg></div>

  <h1 class="hero-question display">EXPERIENCES THAT MAKE<br>YOU TELL AN UNFORGETTABLE STORY</h1>
  <p class="hero-sub display">INCORPORATED WITH CLIMATE AWARENESS</p>

  <div class="thumb-btn thumb-down">
    <svg width="38" height="36" viewBox="0 0 32 30"><g transform="rotate(180 16 15)"><rect x="1" y="12" width="7" height="17" fill="#fff"/><path d="M10 13l6-11c2 0 3 1.5 2.5 4L17 11h10c2 0 3 1.5 2.6 3.2l-2.5 11.5c-.3 1.6-1.6 2.8-3.2 2.8H10z" fill="#fff"/></g></svg></div>

  <div class="thumb-btn thumb-reset">
    <svg width="44" height="44" viewBox="0 0 40 40"><path d="M31 22a11 11 0 1 1-3.5-10" fill="none" stroke="#fff" stroke-width="3.2" stroke-linecap="round"/><path d="M30 5v9h-9" fill="none" stroke="#fff" stroke-width="3.2" stroke-linecap="round" stroke-linejoin="round"/></svg></div>
</section>

<!-- filters -->
<div class="filter-head">CHOOSE YOUR FILTER
  <svg width="18" height="18" viewBox="0 0 18 18"><path d="M1 2h16l-6 7v7l-4-2V9z" fill="none" stroke="#fff" stroke-width="2" stroke-linejoin="round"/></svg></div>
<aside class="filter-panel">
  <div class="filter-row" style="top:24px">DESTINATIONS<span class="chev">›</span></div>
  <div class="filter-sep" style="top:66px"></div>
  <div class="filter-row" style="top:90px">RESULTS<span class="chev">›</span></div>
  <div class="filter-sep" style="top:130px"></div>
  <div class="cat-head">CATEGORIES</div>
  <div class="cat-row" style="top:207px">Health &amp; Wellness<span class="chev">›</span></div>
  <div class="filter-sep" style="left:36px;width:200px;top:242px"></div>
  <div class="cat-row" style="top:256px">Culinary<span class="chev">›</span></div>
  <div class="filter-sep" style="left:36px;width:200px;top:292px"></div>
  <div class="cat-row" style="top:305px;color:var(--orange);font-weight:600">Safaris<span style="font-size:12px">⌄</span></div>
  <div class="cat-row" style="top:349px;justify-content:flex-start;gap:4px;font-size:14px;color:#777"><span style="width:19px;height:19px;border:1.5px solid #555;border-radius:3px;display:block"></span>Wildlife</div>
  <div class="filter-sep" style="left:36px;width:200px;top:388px"></div>
  <div class="cat-row" style="top:404px">Ranch<span class="chev">›</span></div>
  <div class="filter-row" style="top:469px">DURATION<span class="chev">›</span></div>
  <div class="filter-sep" style="top:513px"></div>
  <div class="filter-row" style="top:535px">BUDGET<span class="chev">›</span></div>
</aside>

<!-- results bar -->
<div class="results-count">Showing 1–8 OF 24 results</div>
<div class="view-grid"><svg width="14" height="14" viewBox="0 0 14 14" fill="#fff"><rect width="6" height="6" rx="1"/><rect x="8" width="6" height="6" rx="1"/><rect y="8" width="6" height="6" rx="1"/><rect x="8" y="8" width="6" height="6" rx="1"/></svg></div>
<div class="view-list"><svg width="24" height="18" viewBox="0 0 24 18"><path d="M0 2h24M0 9h24M0 16h24" stroke="#777" stroke-width="2"/></svg></div>
<div class="sort-label">Sort By:</div>
<div class="sort-select">Deault Sorting<span style="font-size:11px">⌄</span></div>

<!-- card 1 -->
<article class="trip-card" style="top:878px">
  <div class="trip-photo" role="img" aria-label="Giraffe on green savannah beside a traveller in red shawl" style="background:linear-gradient(180deg,#9aa7a3 0%,#8f8e6a 45%,#6f7a44 75%,#4f5c2e 100%)"></div>
  <div class="fav"><svg width="22" height="20" viewBox="0 0 22 20"><path d="M11 19S1 12.5 1 6.2C1 3 3.5 1 6 1c2.2 0 4 1.4 5 3 1-1.6 2.8-3 5-3 2.5 0 5 2 5 5.2C21 12.5 11 19 11 19z" fill="var(--orange)"/></svg></div>
  <h2 class="trip-title display">3 DAYS BIG FIVE TENTED SAFARI, KRUGER NATIONAL<br>PARK, SOUTH AFRICA</h2>
  <div class="trip-price">from<b>€370.00</b></div>
  <div class="card-rule"></div><div class="col-rule"></div>
  <div class="price-for">Price for:</div>
  <ul class="facts">
    <li><svg width="14" height="13" viewBox="0 0 14 13"><rect x=".5" y="1.5" width="13" height="11" fill="none" stroke="#aaa"/><path d="M.5 4.5h13" stroke="#aaa"/></svg>3 days / 2 nights</li>
    <li><svg width="14" height="14" viewBox="0 0 14 14" fill="#999"><circle cx="7" cy="4" r="3"/><path d="M1 14c0-4 3-6 6-6s6 2 6 6z"/></svg>Minimum number of persons: 1</li>
    <li><svg width="14" height="14" viewBox="0 0 14 14" fill="#999"><circle cx="7" cy="4" r="3"/><path d="M1 14c0-4 3-6 6-6s6 2 6 6z"/></svg>Maximum group size: 8</li>
    <li><svg width="14" height="14" viewBox="0 0 14 14" fill="#999"><circle cx="7" cy="4" r="3"/><path d="M1 14c0-4 3-6 6-6s6 2 6 6z"/></svg>Minimum age: 10 years</li>
  </ul>
  <ul class="perks">
    <li><svg width="16" height="14" viewBox="0 0 16 14"><rect x="1" y="3" width="14" height="10" rx="1" fill="none" stroke="#999"/><path d="M5 3V1h6v2" fill="none" stroke="#999"/></svg><span class="lbl">Flexible cancellation policy</span><svg width="13" height="13" viewBox="0 0 13 13"><circle cx="6.5" cy="6.5" r="6.5" fill="var(--green)"/><path d="M3.5 6.8l2 2 4-4.2" fill="none" stroke="#fff" stroke-width="1.6"/></svg></li>
    <li><svg width="16" height="14" viewBox="0 0 16 14"><path d="M1 8l14-6-4 11-3-4z" fill="none" stroke="#999"/></svg><span class="lbl">Airport transfer included</span><svg width="13" height="13" viewBox="0 0 13 13"><circle cx="6.5" cy="6.5" r="6.5" fill="var(--green)"/><path d="M3.5 6.8l2 2 4-4.2" fill="none" stroke="#fff" stroke-width="1.6"/></svg></li>
    <li><svg width="16" height="14" viewBox="0 0 16 14"><path d="M2 13h12M3 10a5 5 0 0 1 10 0zM8 3v2" fill="none" stroke="#999"/></svg><span class="lbl">Meals included</span><svg width="13" height="13" viewBox="0 0 13 13"><circle cx="6.5" cy="6.5" r="6.5" fill="var(--red)"/><path d="M4.2 4.2l4.6 4.6M8.8 4.2L4.2 8.8" stroke="#fff" stroke-width="1.6"/></svg></li>
  </ul>
  <div class="btn-details">SEE DETAILS<svg width="20" height="12" viewBox="0 0 20 12"><path d="M0 6h18M13 1l5 5-5 5" fill="none" stroke="#fff" stroke-width="1.6"/></svg></div>
  <div class="impact" style="left:370px"><svg width="24" height="16" viewBox="0 0 24 16"><path d="M6 15a5 5 0 0 1 0-10 7 7 0 0 1 13 2 4 4 0 0 1 0 8z" fill="#3a86c8"/></svg>3.02 tCO2(e)</div>
  <div class="impact" style="left:527px"><svg width="20" height="16" viewBox="0 0 20 16"><path d="M1 15C3 6 9 2 19 1c-1 9-6 13-13 12z" fill="var(--green)"/></svg>193 trees</div>
</article>

<!-- card 2 -->
<article class="trip-card" style="top:1645px">
  <div class="trip-photo" role="img" aria-label="Cowboy on a chestnut horse herding a calf across a dry pasture" style="background:linear-gradient(180deg,#b7b9b0 0%,#a7a58d 40%,#8a8160 70%,#6f6446 100%)"></div>
  <div class="fav"><svg width="22" height="20" viewBox="0 0 22 20"><path d="M11 19S1 12.5 1 6.2C1 3 3.5 1 6 1c2.2 0 4 1.4 5 3 1-1.6 2.8-3 5-3 2.5 0 5 2 5 5.2C21 12.5 11 19 11 19z" fill="var(--orange)"/></svg></div>
  <h2 class="trip-title display">2 DAYS WILD WEST RANCH EXPLORATION AND BIKE<br>HOLIDAY IN COLORADO, USA</h2>
  <div class="trip-price">from<b>€384.00</b></div>
  <div class="card-rule"></div><div class="col-rule"></div>
  <div class="price-for">Price for:</div>
  <ul class="facts">
    <li><svg width="14" height="13" viewBox="0 0 14 13"><rect x=".5" y="1.5" width="13" height="11" fill="none" stroke="#aaa"/><path d="M.5 4.5h13" stroke="#aaa"/></svg>2 days / 1 nights</li>
    <li><svg width="14" height="14" viewBox="0 0 14 14" fill="#999"><circle cx="7" cy="4" r="3"/><path d="M1 14c0-4 3-6 6-6s6 2 6 6z"/></svg>Minimum number of persons: 1</li>
    <li><svg width="14" height="14" viewBox="0 0 14 14" fill="#999"><circle cx="7" cy="4" r="3"/><path d="M1 14c0-4 3-6 6-6s6 2 6 6z"/></svg>Maximum group size: 5</li>
    <li><svg width="14" height="14" viewBox="0 0 14 14" fill="#999"><circle cx="7" cy="4" r="3"/><path d="M1 14c0-4 3-6 6-6s6 2 6 6z"/></svg>Minimum age: 13 years</li>
  </ul>
  <ul class="perks">
    <li><svg width="16" height="14" viewBox="0 0 16 14"><rect x="1" y="3" width="14" height="10" rx="1" fill="none" stroke="#999"/><path d="M5 3V1h6v2" fill="none" stroke="#999"/></svg><span class="lbl">Flexible cancellation policyl</span><svg width="13" height="13" viewBox="0 0 13 13"><circle cx="6.5" cy="6.5" r="6.5" fill="var(--green)"/><path d="M3.5 6.8l2 2 4-4.2" fill="none" stroke="#fff" stroke-width="1.6"/></svg></li>
    <li><svg width="16" height="14" viewBox="0 0 16 14"><path d="M1 8l14-6-4 11-3-4z" fill="none" stroke="#999"/></svg><span class="lbl">Airport transfer includedl</span><svg width="13" height="13" viewBox="0 0 13 13"><circle cx="6.5" cy="6.5" r="6.5" fill="var(--green)"/><path d="M3.5 6.8l2 2 4-4.2" fill="none" stroke="#fff" stroke-width="1.6"/></svg></li>
    <li><svg width="16" height="14" viewBox="0 0 16 14"><path d="M2 13h12M3 10a5 5 0 0 1 10 0zM8 3v2" fill="none" stroke="#999"/></svg><span class="lbl">Meals included</span><svg width="13" height="13" viewBox="0 0 13 13"><circle cx="6.5" cy="6.5" r="6.5" fill="var(--red)"/><path d="M4.2 4.2l4.6 4.6M8.8 4.2L4.2 8.8" stroke="#fff" stroke-width="1.6"/></svg></li>
  </ul>
  <div class="btn-details">SEE DETAILS<svg width="20" height="12" viewBox="0 0 20 12"><path d="M0 6h18M13 1l5 5-5 5" fill="none" stroke="#fff" stroke-width="1.6"/></svg></div>
  <div class="impact" style="left:370px"><svg width="24" height="16" viewBox="0 0 24 16"><path d="M6 15a5 5 0 0 1 0-10 7 7 0 0 1 13 2 4 4 0 0 1 0 8z" fill="#3a86c8"/></svg>2.51 tCO2(e)</div>
  <div class="impact" style="left:527px"><svg width="20" height="16" viewBox="0 0 20 16"><path d="M1 15C3 6 9 2 19 1c-1 9-6 13-13 12z" fill="var(--green)"/></svg>160 trees</div>
</article>

<!-- card 3 -->
<article class="trip-card" style="top:2411px">
  <div class="trip-photo" role="img" aria-label="Group of riders on white horses crossing a grassy plain under a blue sky" style="background:linear-gradient(180deg,#3f6f93 0%,#6f93a0 30%,#8e9a55 55%,#7d8240 80%,#5b6030 100%)"></div>
  <div class="fav"><svg width="22" height="20" viewBox="0 0 22 20"><path d="M11 19S1 12.5 1 6.2C1 3 3.5 1 6 1c2.2 0 4 1.4 5 3 1-1.6 2.8-3 5-3 2.5 0 5 2 5 5.2C21 12.5 11 19 11 19z" fill="var(--orange)"/></svg></div>
  <h2 class="trip-title display">5 DAYS FULL RANCH EXPERIENCE AND HORSEMANSHIP<br>TRAINING IN MULLA CREEK, NSW, AUSTRALIA</h2>
  <div class="trip-price">from<b>€458.00</b></div>
  <div class="card-rule"></div><div class="col-rule"></div>
  <div class="price-for">Price for:</div>
  <ul class="facts">
    <li><svg width="14" height="13" viewBox="0 0 14 13"><rect x=".5" y="1.5" width="13" height="11" fill="none" stroke="#aaa"/><path d="M.5 4.5h13" stroke="#aaa"/></svg>5 days / 4 nights</li>
    <li><svg width="14" height="14" viewBox="0 0 14 14" fill="#999"><circle cx="7" cy="4" r="3"/><path d="M1 14c0-4 3-6 6-6s6 2 6 6z"/></svg>Minimum number of persons: 1</li>
    <li><svg width="14" height="14" viewBox="0 0 14 14" fill="#999"><circle cx="7" cy="4" r="3"/><path d="M1 14c0-4 3-6 6-6s6 2 6 6z"/></svg>Maximum group size: 15</li>
    <li><svg width="14" height="14" viewBox="0 0 14 14" fill="#999"><circle cx="7" cy="4" r="3"/><path d="M1 14c0-4 3-6 6-6s6 2 6 6z"/></svg>Minimum age: 15 years</li>
  </ul>
  <ul class="perks">
    <li><svg width="16" height="14" viewBox="0 0 16 14"><rect x="1" y="3" width="14" height="10" rx="1" fill="none" stroke="#999"/><path d="M5 3V1h6v2" fill="none" stroke="#999"/></svg><span class="lbl">Flexible cancellation policyl</span><svg width="13" height="13" viewBox="0 0 13 13"><circle cx="6.5" cy="6.5" r="6.5" fill="var(--green)"/><path d="M3.5 6.8l2 2 4-4.2" fill="none" stroke="#fff" stroke-width="1.6"/></svg></li>
    <li><svg width="16" height="14" viewBox="0 0 16 14"><path d="M1 8l14-6-4 11-3-4z" fill="none" stroke="#999"/></svg><span class="lbl">Airport transfer includedl</span><svg width="13" height="13" viewBox="0 0 13 13"><circle cx="6.5" cy="6.5" r="6.5" fill="var(--green)"/><path d="M3.5 6.8l2 2 4-4.2" fill="none" stroke="#fff" stroke-width="1.6"/></svg></li>
    <li><svg width="16" height="14" viewBox="0 0 16 14"><path d="M2 13h12M3 10a5 5 0 0 1 10 0zM8 3v2" fill="none" stroke="#999"/></svg><span class="lbl">Meals included</span><svg width="13" height="13" viewBox="0 0 13 13"><circle cx="6.5" cy="6.5" r="6.5" fill="var(--red)"/><path d="M4.2 4.2l4.6 4.6M8.8 4.2L4.2 8.8" stroke="#fff" stroke-width="1.6"/></svg></li>
  </ul>
  <div class="btn-details">SEE DETAILS<svg width="20" height="12" viewBox="0 0 20 12"><path d="M0 6h18M13 1l5 5-5 5" fill="none" stroke="#fff" stroke-width="1.6"/></svg></div>
  <div class="impact" style="left:370px"><svg width="24" height="16" viewBox="0 0 24 16"><path d="M6 15a5 5 0 0 1 0-10 7 7 0 0 1 13 2 4 4 0 0 1 0 8z" fill="#3a86c8"/></svg>5.26 tCO2(e)</div>
  <div class="impact" style="left:527px"><svg width="20" height="16" viewBox="0 0 20 16"><path d="M1 15C3 6 9 2 19 1c-1 9-6 13-13 12z" fill="var(--green)"/></svg>335 trees</div>
</article>

<!-- pagination -->
<div class="abs pager pg-prev">‹ Prev</div>
<span class="pg-num" style="left:858px">1</span>
<div class="pg-active">2</div>
<span class="pg-num" style="left:935px">3</span>
<span class="pg-num" style="left:962px">…</span>
<span class="pg-num" style="left:989px">82</span>
<div class="abs pager pg-next">Next ›</div>

<footer class="site-footer"></footer>

<!-- impact charts -->
<section class="impact-card" style="left:87px">
  <h3 class="impact-title display">CARBON FOOTPRINT</h3>
  <p class="impact-sub">Total carbon footprint from booked vacations on our site</p>
  <svg class="abs" style="left:0;top:140px" width="494" height="220" viewBox="0 0 494 220">
    <path d="M112 95v26a118 40 0 0 0 236 0V95" fill="var(--teal-dark)"/>
    <ellipse cx="230" cy="95" rx="118" ry="40" fill="var(--teal)"/>
    <path d="M230 95L112 95A118 40 0 0 1 345 88Z" fill="var(--orange)"/>
    <path d="M230 95L345 88A118 40 0 0 1 348 101Z" fill="var(--blue)"/>
    <path d="M235 56V38h12M348 92h34M215 136v22h-12" fill="none" stroke="#999" stroke-width=".8"/>
    <text x="250" y="41" font-size="9" fill="#666" font-family="Poppins,sans-serif">2.11 KtCO2(e)</text>
    <text x="385" y="95" font-size="9" fill="#666" font-family="Poppins,sans-serif">158 tCO2(e)</text>
    <text x="152" y="161" font-size="9" fill="#666" font-family="Poppins,sans-serif">3.01 KtCO2(e)</text>
  </svg>
  <div class="legend"><i style="background:var(--blue)"></i>Yet to offset, 2.99% <span style="margin-left:110px"><i style="background:var(--orange)"></i>Offset total by Velqorambe, 40%</span><br><i style="background:var(--teal)"></i>Offset total by customers, 57.01%</div>
</section>

<section class="impact-card" style="left:617px">
  <h3 class="impact-title display">TRESS</h3>
  <p class="impact-sub">Total trees to offset booked vacations on our site</p>
  <svg class="abs" style="left:0;top:140px" width="494" height="220" viewBox="0 0 494 220">
    <path d="M79 95v26a118 40 0 0 0 236 0V95" fill="var(--teal-dark)"/>
    <ellipse cx="197" cy="95" rx="118" ry="40" fill="var(--teal)"/>
    <path d="M197 95L79 95A118 40 0 0 1 312 88Z" fill="var(--orange)"/>
    <path d="M197 95L312 88A118 40 0 0 1 315 101Z" fill="var(--blue)"/>
    <path d="M240 57V38h12M315 92h34M180 136v22h-12" fill="none" stroke="#999" stroke-width=".8"/>
    <text x="255" y="41" font-size="9" fill="#666" font-family="Poppins,sans-serif">576 trees</text>
    <text x="352" y="95" font-size="9" fill="#666" font-family="Poppins,sans-serif">43 trees</text>
    <text x="126" y="161" font-size="9" fill="#666" font-family="Poppins,sans-serif">821 trees</text>
  </svg>
  <div class="legend"><i style="background:var(--blue)"></i>Yet to plant trees, 2.99% <span style="margin-left:100px"><i style="background:var(--orange)"></i>Planted by Velqorambe, 40%</span><br><i style="background:var(--teal)"></i>Planted by customers, 57.01%</div>
</section>

<!-- footer columns -->
<div class="foot-col" style="left:87px;width:185px">
  <h4>LEGAL INFORMATION</h4>
  VELQORAMBE B.V. is registered with the trade register of the Chamber of Commerce in Utrecht, the Netherlands, under registration number 58203917.<br>VAT registration number is NL204517739B02.
</div>
<div class="foot-col" style="left:328px">
  <h4>VELQORAMBE</h4>
  About Us<br>Contact Us<br>Terms and Conditions<br>Privacy
</div>
<div class="foot-col" style="left:530px">
  <h4>SUSTAINABILITY</h4>
  Our Climate Pledge<br>Our Progress<br>How It Works
</div>
<div class="foot-col" style="left:726px">
  <h4>PARTNERS</h4>
  Organizers<br>Canopyfund.org
</div>
<div class="foot-col" style="left:889px">
  <h4>CONTACT</h4>
  <div class="contact-row"><svg width="14" height="13" viewBox="0 0 14 13"><path d="M7 0l7 6h-2v7H9V9H5v4H2V6H0z" fill="var(--orange)"/></svg>Amsterdam, the Netherlands</div>
  <div class="contact-row"><svg width="14" height="11" viewBox="0 0 14 11"><rect width="14" height="11" rx="1" fill="var(--orange)"/><path d="M1 1l6 5 6-5" fill="none" stroke="#212121" stroke-width="1.2"/></svg>info@velqorambe.com</div>
  <div class="contact-row"><svg width="13" height="13" viewBox="0 0 13 13"><path d="M3 0l2.5 3.2-1.5 1.6a8 8 0 0 0 4.2 4.2l1.6-1.5L13 10l-1.5 2.6C6 13 0 7 .4 1.5z" fill="var(--orange)"/></svg>+ 01 555 018 42</div>
  <div class="socials"><span></span><span></span><span></span><span></span></div>
</div>
<div class="foot-rule"></div>
<div class="copyright">© 2020 VELQORAMBE B.V. ALL RIGHTS RESERVED</div>
<div class="to-top"><svg width="14" height="9" viewBox="0 0 14 9"><path d="M1 8l6-6 6 6" fill="none" stroke="#fff" stroke-width="2"/></svg></div>

</body>
</html>
```